Website Design for an Exciting & Sophisticated Premium CBD Company.

Design a responsive Website with the following goals in mind:
-      Main theme for the site will be based on the Tall Harbor Pebblegate theme.  Please use this when designing for ease of integration.  You can see our current site to gain more insight.  quillorcbd.example
-	Build trust with website visitors with an engaging, informative content driven website, that leads to a conversion of product purchase and repeat business.
-	The website will embody a lifestyle feel and make the visitor identify with the content or emphasize with the life they used to have or believe they can have by using our products
-	The website will allow for super charged SEO and other digital marketing and advertising strategies and tactics used to increase discovery, awareness, and conversion.
Please see additional goals in the uploaded files.

Target Market(s)
Male/Female 25-50
Number of Pages Required
1 page
Font styles to use
Other font styles liked:
- Monserrat is the company Font. Please use throughout. Regular, Bold, Semi-Bold, light
Requirements
Must have
- Please see attached document for this information
Nice to have
Should not have

```html
<!DOCTYPE html>
<html lang="en">
<head>
<meta charset="utf-8">
<title>Quillor CBD</title>
<link rel="stylesheet" href="https://fonts.googleapis.com/css2?family=Montserrat:wght@300;400;500;600;700;800&display=swap">
<style>
:root{
  --gold:#E8C97A;
  --gold-deep:#D9B25C;
  --gold-text:#CFA84E;
  --ink:#1E1E1E;
  --band:#262626;
  --muted:#555;
  --white:#fff;
  --leaf:#2F7A46;
}
*{margin:0;padding:0;box-sizing:border-box}
html,body{width:1200px;height:2880px;overflow:hidden}
body{font-family:"Montserrat",sans-serif;color:var(--ink);background:var(--white);position:relative}
.abs{position:absolute}

/* hero */
.hero{position:absolute;left:0;top:0;width:1200px;height:548px;background:var(--gold);overflow:hidden}
.watermark{position:absolute;left:20px;top:150px;font-size:250px;font-weight:800;color:rgba(255,255,255,.18);letter-spacing:4px;line-height:1}
.brand{position:absolute;display:flex;align-items:center;gap:8px;font-weight:600;color:var(--gold-text);letter-spacing:2px}
.brand-dot{width:12px;height:12px;border-radius:50%;background:var(--gold-text)}
.hero .brand{left:235px;top:50px;font-size:15px;color:#B88A2E}
.hero .brand .brand-dot{background:#B88A2E}
.nav{position:absolute;top:53px;font-size:9.5px;font-weight:600;letter-spacing:.3px}
.search{position:absolute;left:859px;top:48px;width:105px;height:21px;border-radius:11px;background:var(--ink);color:#ddd;font-size:9px;padding:5px 13px}
.hero-title{position:absolute;left:235px;top:166px;font-size:58px;font-weight:700;letter-spacing:-.5px}
.hero-sub{position:absolute;left:232px;top:246px;font-size:30px;font-weight:600;line-height:36px}
.rule{position:absolute;height:3px;background:var(--ink)}
.hero-copy{position:absolute;left:235px;top:350px;width:380px;font-size:12.5px;line-height:19px;letter-spacing:.4px}
.btn{position:absolute;display:flex;align-items:center;justify-content:center;border-radius:18px;font-size:10.5px;font-weight:600}
.btn-dark{background:var(--ink);color:var(--gold)}
.btn-gold{background:var(--gold);color:var(--white)}
.btn-outline{border:1.5px solid var(--gold);color:var(--gold)}
.ph{position:absolute}
.dot{position:absolute;width:6px;height:6px;border-radius:50%;background:#9a9a9a}
.dot.on{width:9px;height:9px;background:var(--ink)}

/* sections */
.sec-title{position:absolute;width:1200px;text-align:center;font-size:22px;font-weight:700;letter-spacing:1.5px}
.vline{position:absolute;left:599px;width:3px;background:var(--ink)}
.about-head{position:absolute;left:486px;top:770px;font-size:31px;font-weight:500;line-height:37.5px;width:490px}
.about-copy{position:absolute;left:486px;top:953px;width:360px;font-size:12.5px;line-height:19px;color:var(--muted);letter-spacing:.4px}

.card{position:absolute;top:1377px;width:230px;height:275px;background:var(--white);border-radius:10px;box-shadow:0 4px 18px rgba(0,0,0,.07);text-align:center}
.card .ph{left:80px;top:37px;width:72px;height:72px;border-radius:12px;background:linear-gradient(135deg,#F4E3B8,#E8C97A)}
.card h3{position:absolute;top:138px;width:100%;font-size:15px;font-weight:600}
.card p{position:absolute;top:166px;left:15px;width:200px;font-size:11.5px;line-height:19px}
.card .btn{left:42px;top:219px;width:146px;height:35px;font-weight:500}

.band{position:absolute;left:0;top:1842px;width:1200px;height:296px;background:var(--band)}
.band-head{position:absolute;width:1200px;text-align:center;color:var(--white);font-size:30px;font-weight:600;line-height:45px;top:1888px}
.band-head em{font-style:normal;color:var(--gold)}
.band-copy{position:absolute;left:400px;top:1994px;width:400px;text-align:center;color:var(--white);font-size:12.5px;line-height:19px;letter-spacing:.4px}

.feature{position:absolute;top:2365px;width:130px;text-align:center}
.feature .ph{position:relative;margin:0 auto;width:66px;height:66px;border-radius:50%;background:linear-gradient(135deg,#F6E8C4,#E8C97A)}
.feature span{display:block;margin-top:20px;font-size:9.5px;font-weight:700;line-height:11px}

/* footer */
.footer-line{position:absolute;left:0;top:2606px;width:1200px;height:1px;background:#e4e4e4}
.col{position:absolute;top:2646px;font-size:10px;line-height:18.8px;color:#333}
.col h4{font-size:11px;font-weight:600;margin-bottom:1px;letter-spacing:.5px}
.social{position:absolute;top:2775px;width:25px;height:25px;border-radius:50%}
.copyright{position:absolute;top:2851px;width:1200px;text-align:center;font-size:8.5px;color:#333}
.strip{position:absolute;left:0;top:2873px;width:1200px;height:7px;background:var(--gold)}
</style>
</head>
<body>

<section class="hero">
  <div class="watermark">QUILLOR</div>
  <div class="ph" role="img" aria-label="Green leaves in the top left corner" style="left:-40px;top:-30px;width:160px;height:150px;border-radius:50%;background:radial-gradient(circle,#3E8F55,#2F7A46 60%,rgba(47,122,70,0) 72%)"></div>
  <div class="ph" role="img" aria-label="Green leaves along the right edge" style="left:1080px;top:140px;width:190px;height:420px;border-radius:50%;background:radial-gradient(ellipse,#3E8F55,#2F7A46 55%,rgba(47,122,70,0) 72%)"></div>

  <div class="brand"><span class="brand-dot"></span>QUILLOR</div>
  <span class="nav" style="left:427px">SHOP</span>
  <span class="nav" style="left:484px">DROPS</span>
  <span class="nav" style="left:547px">TOPICALS</span>
  <span class="nav" style="left:616px">SIGN</span>
  <span class="nav" style="left:666px">REGISTER</span>
  <span class="nav" style="left:775px">CART</span>
  <svg class="abs" style="left:817px;top:48px" width="20" height="22" viewBox="0 0 20 22"><path d="M3 7h12l1 12H2z" fill="none" stroke="#1E1E1E" stroke-width="1.3"/><path d="M6 7V5a3 3 0 0 1 6 0v2" fill="none" stroke="#1E1E1E" stroke-width="1.3"/><circle cx="15" cy="17" r="4" fill="#1E1E1E"/></svg>
  <div class="search">Search
    <svg class="abs" style="right:11px;top:5px" width="11" height="11" viewBox="0 0 11 11"><circle cx="4.5" cy="4.5" r="3.5" fill="none" stroke="#E8C97A" stroke-width="1.3"/><path d="M7 7l3 3" stroke="#E8C97A" stroke-width="1.3"/></svg>
  </div>

  <div class="hero-title">QUILLOR</div>
  <div class="rule" style="left:0;top:230px;width:330px"></div>
  <div class="hero-sub">IS NOT YOUR EVERYDAY<br>CBD, QUILLOR IS A LIFSTYLE.</div>
  <div class="rule" style="left:509px;top:321px;width:210px"></div>
  <p class="hero-copy">QUILLOR is about incorporating into your daily routine to be the best you. Focus on flavor, effects and only quality ingredients.</p>
  <div class="btn btn-dark" style="left:235px;top:434px;width:143px;height:34px">Read More</div>

  <div class="abs" style="left:43px;top:413px;width:192px;height:192px;border-radius:50%;background:rgba(0,0,0,.06)"></div>
  <div class="ph" role="img" aria-label="Black dropper bottle of calming CBD oil" style="left:95px;top:285px;width:89px;height:296px;border-radius:22px 22px 10px 10px;background:linear-gradient(90deg,#111,#2c2c2c 50%,#111)"></div>

  <svg class="abs" style="left:664px;top:147px" width="376" height="376" viewBox="0 0 376 376"><circle cx="188" cy="188" r="185" fill="none" stroke="#8a7340" stroke-dasharray="4 4"/><circle cx="188" cy="188" r="168" fill="none" stroke="#8a7340" stroke-dasharray="4 4"/></svg>
  <div class="ph" role="img" aria-label="Black dropper bottle of energising CBD oil" style="left:799px;top:129px;width:112px;height:357px;border-radius:26px 26px 12px 12px;background:linear-gradient(90deg,#0f0f0f,#2e2e2e 50%,#0f0f0f)"></div>
  <div class="ph" role="img" aria-label="Small tilted dropper bottle" style="left:1055px;top:440px;width:50px;height:140px;border-radius:14px;background:#151515;transform:rotate(35deg)"></div>

  <span class="dot" style="left:565px;top:516px"></span>
  <span class="dot" style="left:580px;top:516px"></span>
  <span class="dot on" style="left:600px;top:514px"></span>
  <span class="dot" style="left:622px;top:516px"></span>
</section>

<section class="about">
  <h2 class="sec-title" style="top:620px">ABOUT US</h2>
  <div class="rule" style="left:483px;top:654px;width:69px"></div>
  <div class="abs" style="left:156px;top:962px;width:236px;height:236px;border-radius:50%;background:var(--gold)"></div>
  <div class="ph" role="img" aria-label="Phone showing the brand app with an energising oil bottle" style="left:235px;top:702px;width:199px;height:410px;border-radius:22px;border:6px solid #111;background:linear-gradient(180deg,#fff 60%,#E8C97A 60%)"></div>
  <h3 class="about-head">QUILLOR CBD was born out of a drive for a better life. Created to enable the extraordinary in us all through the use of CBD.</h3>
  <p class="about-copy">QUILLOR stands for fun, excitement, joy, and happiness, all the qualities that promote the best feeling and overall wellbeing.</p>
  <div class="btn btn-gold" style="left:486px;top:1049px;width:144px;height:33px">Read More</div>
  <div class="vline" style="top:1146px;height:69px"></div>
</section>

<section class="drops">
  <h2 class="sec-title" style="top:1290px">SHOP DROPS</h2>
  <div class="rule" style="left:460px;top:1324px;width:68px"></div>
  <article class="card" style="left:235px">
    <div class="ph" role="img" aria-label="Line icon of art tools in a cloud"></div>
    <h3>Creativity is Calling.....</h3>
    <p>Our most popular profile is back in stock.</p>
    <div class="btn btn-outline">Shop Q Bright</div>
  </article>
  <article class="card" style="left:484px">
    <div class="ph" role="img" aria-label="Line icon of art tools in a cloud"></div>
    <h3>Creativity is Calling.....</h3>
    <p>Our most popular profile is back in stock.</p>
    <div class="btn btn-outline">Shop Q Bright</div>
  </article>
  <article class="card" style="left:733px">
    <div class="ph" role="img" aria-label="Line icon of art tools in a cloud"></div>
    <h3>Creativity is Calling.....</h3>
    <p>Our most popular profile is back in stock.</p>
    <div class="btn btn-outline">Shop Q Bright</div>
  </article>
  <span class="dot" style="left:573px;top:1698px"></span>
  <span class="dot on" style="left:593px;top:1696px"></span>
  <span class="dot" style="left:614px;top:1698px"></span>
  <div class="vline" style="top:1735px;height:68px"></div>
</section>

<section class="lifestyle">
  <div class="band"></div>
  <div class="ph" role="img" aria-label="Faint row of dropper bottles in the background" style="left:0;top:1842px;width:1200px;height:296px;background:linear-gradient(90deg,rgba(255,255,255,.03),rgba(255,255,255,.07),rgba(255,255,255,.03))"></div>
  <h2 class="band-head"><em>QUILLOR</em> is not your everyday CBD,<br>QUILLOR is a lifestyle.</h2>
  <div class="abs" style="left:0;top:1931px;width:622px;height:3px;background:var(--gold)"></div>
  <div class="abs" style="left:634px;top:1978px;width:294px;height:3px;background:var(--gold)"></div>
  <p class="band-copy">QUILLOR is about incorporating into your daily routine to be the best you. Focus on flavor, effects and only quality ingredients.</p>
  <div class="btn btn-gold" style="left:527px;top:2075px;width:143px;height:33px">Read More</div>
  <div class="ph" role="img" aria-label="Black dropper bottle of calming CBD oil" style="left:1004px;top:1929px;width:89px;height:290px;border-radius:22px 22px 10px 10px;background:linear-gradient(90deg,#0f0f0f,#2e2e2e 50%,#0f0f0f)"></div>
  <div class="vline" style="top:2211px;height:70px"></div>
</section>

<section class="features">
  <div class="feature" style="left:217px"><div class="ph" role="img" aria-label="Leaf icon"></div><span>ZERO THC</span></div>
  <div class="feature" style="left:324px"><div class="ph" role="img" aria-label="Lab flask icon"></div><span>3RD PARTY LAB<br>TESTED</span></div>
  <div class="feature" style="left:460px"><div class="ph" role="img" aria-label="Crossed out spray bottle icon"></div><span>FREE OF PESTICIDES<br>+ SOLVENTS</span></div>
  <div class="feature" style="left:591px"><div class="ph" role="img" aria-label="Spectrum circle icon"></div><span>BROAD SPECTRUM<br>HEMP CBD</span></div>
  <div class="feature" style="left:704px"><div class="ph" role="img" aria-label="Crossed out DNA icon"></div><span>NON GMO</span></div>
  <div class="feature" style="left:832px"><div class="ph" role="img" aria-label="Stars and stripes globe icon"></div><span>100% SOURCED + MADE<br>IN THE USA</span></div>
</section>

<footer>
  <div class="footer-line"></div>
  <div class="ph" role="img" aria-label="Soft grey leaves in the lower right corner" style="left:1090px;top:2600px;width:150px;height:280px;border-radius:50%;background:radial-gradient(ellipse,#cfcfcf,rgba(220,220,220,0) 70%)"></div>
  <div class="brand" style="left:61px;top:2645px;font-size:17px"><span class="brand-dot"></span>QUILLOR</div>
  <div class="col" style="left:235px"><h4>Navigate</h4>FDA Disclosure<br>Privacy Policy<br>Terms and Conditions<br>Why Quillor CBD<br>Quillor Ambassadors<br>Quillor Cares<br>Shipping &amp; Returns<br>Contact Us<br>Sitemap</div>
  <div class="col" style="left:385px"><h4>Categories</h4>Shop<br>Drops<br>Topicals</div>
  <div class="col" style="left:534px"><h4>Info</h4>4210 Meadow Lane<br>Aldenbrook TX 75000</div>
  <div class="col" style="left:684px"><h4>Subscribe to our newsletter</h4>Get the latest updates on new products and upcoming sales</div>
  <div class="abs" style="left:700px;top:2719px;font-size:8.5px;color:#888">Your email address</div>
  <div class="abs" style="left:684px;top:2740px;width:200px;height:1px;background:#eee"></div>
  <div class="btn" style="left:889px;top:2711px;width:75px;height:28px;border-radius:4px;background:var(--ink);color:var(--white);font-size:9.5px">Subscribe</div>
  <span class="social" style="left:685px;background:#3a5a98"></span>
  <span class="social" style="left:735px;background:#4fa8e0"></span>
  <span class="social" style="left:783px;background:#1f6fa8"></span>
  <span class="social" style="left:829px;background:#c8232c"></span>
  <div class="copyright">© 2020 Quillor CBD</div>
  <div class="strip"></div>
</footer>

</body>
</html>
```